Corvane QXL Facebook Landing Page

Complete redesign our 2012 Facebook site (currently not published), mirroring the look and feel of our corporate website -colors, tone.

www.corvaneqxl.com

Target Market(s)

B2B

Industry/Entity Type

Information Technology

Font styles to use
Sans Serif

Colors
f68d4d
f78f20

```html
<!DOCTYPE html>
<html lang="en">
<head>
<meta charset="utf-8">
<title>Corvane QXL – Social Landing Page</title>
<link rel="stylesheet" href="https://fonts.googleapis.com/css2?family=Montserrat:wght@600;700;800&family=Roboto:wght@400;500;700&display=swap">
<style>
  :root {
    --brand-orange: #f78f20;
    --brand-peach: #f68d4d;
    --ink: #1d2129;
    --muted: #90949c;
    --link: #365899;
    --bar-blue: #4267b2;
    --bar-blue-dark: #29487d;
    --page-bg: #e9ebee;
    --card-bg: #ffffff;
    --card-line: #dddfe2;
    --cta-blue: #4080ff;
    --cta-green: #42b72a;
    --cover-black: #0b0b0c;
    --placeholder: #8a8d91;
  }
  * { box-sizing: border-box; margin: 0; padding: 0; }
  html, body { width: 1200px; height: 820px; overflow: hidden; }
  body {
    background: var(--page-bg);
    font-family: "Roboto", Arial, sans-serif;
    color: var(--ink);
    font-size: 12px;
    position: relative;
  }

  /* top navigation bar */
  .top-bar {
    position: absolute; left: 0; top: 0; width: 1200px; height: 48px;
    background: var(--bar-blue);
    border-bottom: 1px solid var(--bar-blue-dark);
  }
  .top-bar__mark {
    position: absolute; left: 270px; top: 11px; width: 26px; height: 26px;
    background: #fff; border-radius: 3px;
  }
  .top-bar__search {
    position: absolute; left: 302px; top: 11px; width: 320px; height: 26px;
    background: #fff; border-radius: 3px;
  }
  .top-bar__links {
    position: absolute; left: 660px; top: 0; height: 48px;
    display: flex; align-items: center; gap: 16px;
    color: #fff; font-weight: 700; font-size: 12px;
  }
  .top-bar__avatar { width: 22px; height: 22px; background: var(--cover-black); border-radius: 2px; }
  .top-bar__icon { width: 16px; height: 16px; border-radius: 50%; background: rgba(255,255,255,.55); }

  /* left column */
  .page-identity { position: absolute; left: 272px; top: 64px; width: 128px; }
  .profile-logo {
    width: 126px; height: 126px; background: var(--cover-black);
    border: 3px solid #fff; box-shadow: 0 0 0 1px var(--card-line);
    display: flex; flex-direction: column; align-items: center; justify-content: center; gap: 6px;
  }
  .profile-logo__name {
    font-family: "Montserrat", sans-serif; font-weight: 800; font-size: 15px;
    color: #fff; letter-spacing: .3px; text-align: center; line-height: 1.05;
  }
  .profile-logo__tag { font-family: "Montserrat", sans-serif; font-size: 7.5px; font-weight: 600; color: var(--brand-orange); white-space: nowrap; }
  .page-title {
    margin-top: 14px; font-size: 16px; font-weight: 500; white-space: nowrap;
    display: flex; align-items: center; gap: 5px;
  }
  .verified { width: 13px; height: 13px; flex: none; }
  .page-handle { color: var(--muted); font-size: 11px; margin-top: 2px; }
  .page-nav { list-style: none; margin-top: 18px; }
  .page-nav li { font-size: 12px; color: #4b4f56; padding: 7px 8px; }
  .page-nav li.is-active { font-weight: 700; color: var(--ink); border-left: 3px solid var(--bar-blue); padding-left: 5px; background: #f6f7f9; }
  .create-page {
    margin: 12px 8px 0; display: inline-block; background: var(--cta-green); color: #fff;
    font-weight: 700; font-size: 10px; padding: 5px 9px; border-radius: 2px;
  }

  /* cover */
  .cover {
    position: absolute; left: 405px; top: 64px; width: 528px; height: 250px;
    background: var(--cover-black); overflow: hidden;
  }
  .cover__art {
    position: absolute; left: 140px; top: 0; width: 388px; height: 250px;
    background:
      radial-gradient(circle at 55% 45%, rgba(255,200,110,.95) 0 6%, rgba(247,143,32,.7) 16%, rgba(160,70,10,.45) 34%, rgba(11,11,12,0) 60%),
      linear-gradient(90deg, var(--cover-black) 0%, #2a1406 40%, #3a1c08 70%, #140a04 100%);
  }
  .cover__brand { position: absolute; left: 24px; top: 36px; }
  .cover__name {
    font-family: "Montserrat", sans-serif; font-weight: 800; font-size: 26px; color: #fff; line-height: 1;
  }
  .cover__subtitle { margin-top: 12px; color: #fff; font-size: 15px; font-weight: 400; }
  .cover__motto {
    position: absolute; left: 24px; top: 146px;
    font-family: "Montserrat", sans-serif; font-weight: 800; font-size: 17px; line-height: 1.15; color: #fff;
  }

  .action-row {
    position: absolute; left: 405px; top: 324px; width: 528px; height: 30px;
    display: flex; align-items: center; gap: 6px;
  }
  .action-btn {
    height: 24px; padding: 0 10px; background: #f6f7f9; border: 1px solid #ced0d4; border-radius: 2px;
    font-size: 10px; font-weight: 700; color: #4b4f56; display: flex; align-items: center;
  }
  .sign-up {
    margin-left: auto; width: 176px; height: 24px; background: var(--cta-blue); color: #fff; border-radius: 2px;
    font-weight: 700; font-size: 11px; display: flex; align-items: center; justify-content: center;
  }

  /* cards */
  .card { background: var(--card-bg); border: 1px solid var(--card-line); border-radius: 3px; position: absolute; }
  .status-card { left: 405px; top: 364px; width: 320px; height: 88px; }
  .status-card__head { height: 28px; border-bottom: 1px solid var(--card-line); background: #f6f7f9; padding: 0 10px; display: flex; align-items: center; font-weight: 700; font-size: 11px; }
  .status-card__body { display: flex; align-items: center; gap: 10px; padding: 14px 10px; color: var(--muted); font-size: 11px; }
  .mini-avatar { width: 32px; height: 32px; background: var(--cover-black); border-bottom: 3px solid var(--brand-orange); flex: none; }

  .post-card { left: 405px; top: 462px; width: 320px; height: 358px; border-bottom: none; }
  .post-card__meta { display: flex; gap: 8px; padding: 10px; }
  .post-card__author { color: var(--link); font-weight: 700; font-size: 12px; }
  .post-card__time { color: var(--muted); font-size: 10px; margin-top: 2px; }
  .post-card__text { padding: 0 10px 10px; font-size: 12px; }
  .post-card__media {
    position: relative; margin: 0 10px; height: 196px;
    background: radial-gradient(ellipse at 20% 70%, rgba(247,143,32,.85) 0%, rgba(140,60,10,.55) 35%, rgba(10,8,6,0) 70%), #0c0a08;
  }
  .post-card__placeholder {
    position: absolute; left: 119px; top: 58px; width: 80px; height: 80px;
    background: var(--placeholder); border-radius: 4px;
  }
  .post-card__actions { display: flex; gap: 26px; padding: 10px 14px; font-size: 11px; color: #606770; font-weight: 700; border-bottom: 1px solid var(--card-line); margin: 0 10px; }
  .post-card__actions .top-comments { margin-left: auto; color: var(--link); font-weight: 400; font-size: 10px; }
  .post-card__stats { display: flex; align-items: center; gap: 6px; padding: 8px 10px; font-size: 11px; color: #606770; }
  .reaction { width: 13px; height: 13px; border-radius: 50%; }
  .reaction--like { background: var(--cta-blue); }
  .reaction--love { background: #f25268; margin-left: -9px; }
  .reaction--wow { background: #f7b125; margin-left: -9px; }
  .post-card__shares { padding: 4px 10px; font-size: 11px; color: #606770; border-top: 1px solid var(--card-line); }

  /* right column */
  .side { position: absolute; left: 737px; top: 364px; width: 196px; }
  .side .card { position: static; margin-bottom: 8px; }
  .side-label { padding: 7px 8px; font-size: 11px; font-weight: 700; }
  .side-search { margin: 0 0 8px; padding: 6px 8px; font-size: 10px; color: var(--muted); background: #fff; border: 1px solid var(--card-line); border-radius: 2px; }
  .side-row { display: flex; align-items: center; gap: 8px; padding: 8px; font-size: 10px; color: #4b4f56; border-bottom: 1px solid #eceef1; }
  .side-row:last-child { border-bottom: none; }
  .side-row__icon { width: 16px; height: 16px; border-radius: 2px; background: var(--cover-black); flex: none; }
  .side-row__icon--invite { background: #ccd0d5; border-radius: 50%; }
  .about-head { display: flex; justify-content: space-between; padding: 7px 8px; font-size: 10px; font-weight: 700; color: #4b4f56; border-bottom: 1px solid var(--card-line); }
  .about-photo { margin: 8px; height: 70px; background: linear-gradient(180deg, #c9d4df 0%, #e4e7ea 45%, #7d858c 100%); }
  .about-line { padding: 4px 8px; font-size: 10px; color: #4b4f56; }
  .about-line--link { color: var(--link); }
  .about-line strong { color: var(--link); display: block; }
  .videos-head { padding: 7px 8px; font-size: 10px; font-weight: 700; color: #4b4f56; }
</style>
</head>
<body>

<header class="top-bar">
  <div class="top-bar__mark"></div>
  <div class="top-bar__search"></div>
  <nav class="top-bar__links">
    <span class="top-bar__avatar"></span>
    <span>Home</span>
    <span>Find Friends</span>
    <span class="top-bar__icon"></span>
    <span class="top-bar__icon"></span>
    <span class="top-bar__icon"></span>
  </nav>
</header>

<aside class="page-identity">
  <div class="profile-logo">
    <span class="profile-logo__name">CORVANE<br>QXL</span>
    <span class="profile-logo__tag">People. Process. Technology.</span>
  </div>
  <h1 class="page-title">Corvane QXL
    <svg class="verified" viewBox="0 0 14 14" aria-hidden="true"><circle cx="7" cy="7" r="7" fill="#4080ff"/><path d="M4 7.2l2 2 4-4.4" fill="none" stroke="#fff" stroke-width="1.6"/></svg>
  </h1>
  <p class="page-handle">@corvaneqxl</p>
  <ul class="page-nav">
    <li class="is-active">Home</li>
    <li>About</li>
    <li>Submit a video!</li>
    <li>Videos</li>
    <li>Likes</li>
    <li>Streamly</li>
    <li>Photos</li>
    <li>Video Channel</li>
    <li>Posts</li>
  </ul>
  <span class="create-page">Create a Page</span>
</aside>

<section class="cover">
  <div class="cover__art" role="img" aria-label="Long-exposure orange light trails spiralling over dark binary code"></div>
  <div class="cover__brand">
    <div class="cover__name">CORVANE QXL</div>
    <div class="cover__subtitle">All-In-One Firm</div>
  </div>
  <div class="cover__motto">PEOPLE.<br>PROCESS.<br>TECHNOLOGY.</div>
</section>

<div class="action-row">
  <span class="action-btn">Liked ▾</span>
  <span class="action-btn">Message</span>
  <span class="action-btn">More ▾</span>
  <span class="sign-up">Sign Up</span>
</div>

<section class="card status-card">
  <div class="status-card__head">Status</div>
  <div class="status-card__body">
    <span class="mini-avatar"></span>
    <span>Write something on this Page...</span>
  </div>
</section>

<article class="card post-card">
  <div class="post-card__meta">
    <span class="mini-avatar"></span>
    <div>
      <div class="post-card__author">Corvane QXL</div>
      <div class="post-card__time">July 22 at 8:01pm · </div>
    </div>
  </div>
  <p class="post-card__text">Lorem ipsum dolor sit amet.</p>
  <div class="post-card__media" role="img" aria-label="Orange light streaks racing through a dark tunnel with an award listing badge">
    <span class="post-card__placeholder"></span>
  </div>
  <div class="post-card__actions">
    <span>Like</span><span>Comment</span><span>Share</span>
    <span class="top-comments">Top Comments ▾</span>
  </div>
  <div class="post-card__stats">
    <span class="reaction reaction--like"></span><span class="reaction reaction--love"></span><span class="reaction reaction--wow"></span>
    <span>2K</span>
  </div>
  <div class="post-card__shares">175 shares</div>
</article>

<aside class="side">
  <div class="card"><div class="side-label">Public Figure</div></div>
  <div class="side-search">Search for posts on this Page</div>
  <div class="card">
    <div class="side-row"><span class="side-row__icon"></span>9,806,321 people like this</div>
    <div class="side-row"><span class="side-row__icon side-row__icon--invite"></span>Invite friends to like this Page</div>
  </div>
  <div class="card">
    <div class="about-head"><span>ABOUT</span><span>›</span></div>
    <div class="about-photo" role="img" aria-label="Modern glass office building with columns under a pale sky"></div>
    <div class="about-line"><strong>Corvane QXL</strong>Lorem ipsum dolor sit amet.</div>
    <div class="about-line about-line--link">www.corvaneqxl.com</div>
    <div class="about-line about-line--link">Legal notice</div>
  </div>
  <div class="card"><div class="videos-head">VIDEOS</div></div>
</aside>

</body>
</html>
```